Präsentationsvorlagen für IT-Systemhaus
Zielgruppe
Wir sind ein IT-Systemhaus, das Beratung und Dienstleistungen für kleine und mittelständische Unternehmen im gesamten deutschsprachigen Raum anbietet. Wir möchten uns gerne eine neue Präsentationsvorlage für PowerPoint erstellen lassen, welche sowohl für Unternehmenspräsentationen, als auch für Kundenpräsentationen im Projektumfeld gut verwendet werden kann.
Aufgabenstellung
Das Design sollte im 16:9 Format angelegt werden. Als Schriftart verwenden Sie bitte OpenSans und ggf. für die Überschriften Armata. Ansonsten sind Sie in der Gestaltung frei.
Vielen Dank für Ihre Mühe!

```html
<!DOCTYPE html>
<html lang="de">
<head>
<meta charset="utf-8">
<title>Präsentationsvorlage PQ-KS GmbH</title>
<link href="https://fonts.googleapis.com/css2?family=Armata&family=Open+Sans:wght@400&display=swap" rel="stylesheet">
<style>
  :root {
    --canvas: #cccccc;
    --red: #a92e2d;
    --white: #ffffff;
    --ink: #555555;
    --ink-soft: #6b6b6b;
    --shadow: 0 1px 4px rgba(0,0,0,0.25);
    --photo-dark: #3a2a22;
    --photo-light: #8a8580;
  }
  * { margin: 0; padding: 0; box-sizing: border-box; }
  html, body { width: 1200px; height: 504px; overflow: hidden; background: var(--canvas); }
  body { position: relative; font-family: "Open Sans", sans-serif; color: var(--ink); }

  .slide { position: absolute; width: 374px; height: 210px; background: var(--white); overflow: hidden; }
  .slide-band { position: absolute; left: 0; top: 0; width: 136px; height: 100%; background: var(--red); }
  .card { position: absolute; top: 16px; width: 329px; height: 178px; background: var(--white); box-shadow: var(--shadow); }

  .brand { position: absolute; display: flex; align-items: center; gap: 2px; font-family: "Armata", sans-serif; font-size: 13px; line-height: 1; color: var(--ink); letter-spacing: -0.3px; }
  .brand-mark { width: 8px; height: 8px; background: var(--red); }
  .brand-suffix { font-size: 3.5px; align-self: flex-end; }

  .heading { position: absolute; font-family: "Armata", sans-serif; color: var(--ink); font-weight: 400; white-space: nowrap; }
  .body-text { position: absolute; font-size: 3.4px; line-height: 1.35; color: var(--ink-soft); }
  .body-text p + p { margin-top: 3px; }

  /* Titelfolie */
  .slide-title { left: 215px; top: 24px; }
  .slide-title .card { left: 22px; }
  .slide-title .heading { left: 56px; top: 78px; font-size: 18px; letter-spacing: 0.6px; }
  .slide-title .lead { position: absolute; left: 56px; top: 106px; width: 210px; font-size: 5.4px; line-height: 1.3; color: var(--ink-soft); }

  /* Abschnittsübersicht */
  .slide-overview { left: 614px; top: 24px; }
  .slide-overview .card { left: 30px; }
  .slide-overview .heading { left: 80px; top: 35px; font-size: 11.5px; letter-spacing: 0.5px; }
  .section { position: absolute; width: 60px; margin-left: -30px; text-align: center; }
  .section-number { display: block; width: 30px; height: 30px; margin: 0 auto; border-radius: 50%; background: var(--red); color: var(--white); font-family: "Armata", sans-serif; font-size: 20px; line-height: 30px; box-shadow: 0 1px 2px rgba(0,0,0,0.3); }
  .section-label { display: block; margin-top: 4px; font-family: "Armata", sans-serif; font-size: 7.6px; letter-spacing: 0.3px; color: var(--ink); }

  /* Textfolie */
  .slide-text { left: 22px; top: 259px; }
  .slide-text .card { left: 31px; }
  .slide-text .heading { left: 53px; top: 70px; font-size: 12px; letter-spacing: 0.5px; }
  .slide-text .body-text { left: 53px; top: 91px; width: 277px; }

  /* Bild-Textfolie */
  .slide-media { left: 421px; top: 259px; }
  .slide-media .card { left: 27px; width: 336px; }
  .photo { position: absolute; left: 27px; top: 16px; width: 137px; height: 178px; background: linear-gradient(160deg, var(--photo-dark) 0%, var(--photo-light) 45%, var(--photo-dark) 100%); }
  .slide-media .heading { left: 176px; top: 59px; font-size: 12px; letter-spacing: 0.5px; }
  .slide-media .body-text { left: 176px; top: 81px; width: 174px; }

  /* Zweispaltige Textfolie */
  .slide-columns { left: 811px; top: 259px; }
  .page { position: absolute; top: 40px; width: 148px; height: 156px; background: var(--white); box-shadow: var(--shadow); }
  .page .body-text { left: 11px; top: 16px; width: 126px; font-size: 3.2px; line-height: 1.55; }
  .page .body-text p + p { margin-top: 5px; }
</style>
</head>
<body>

<section class="slide slide-title">
  <div class="slide-band"></div>
  <div class="card"></div>
  <div class="brand" style="left:275px; top:28px;"><span class="brand-mark"></span>PQ-KS<span class="brand-suffix">GmbH</span></div>
  <h1 class="heading">Titel - Überschrift</h1>
  <p class="lead">Lorem ipsum dolor sit amet, consectetuer adipiscing elit, sed diam nonummy nibh euismod tincidunt ut laoreet dolore magna aliquam erat vo-</p>
</section>

<section class="slide slide-overview">
  <div class="slide-band"></div>
  <div class="card"></div>
  <div class="brand" style="left:283px; top:28px;"><span class="brand-mark"></span>PQ-KS<span class="brand-suffix">GmbH</span></div>
  <h2 class="heading">Abschnittsübersicht</h2>
  <div class="section" style="left:92px; top:72px;"><span class="section-number">1</span><span class="section-label">Überschrift</span></div>
  <div class="section" style="left:177px; top:72px;"><span class="section-number">2</span><span class="section-label">Überschrift</span></div>
  <div class="section" style="left:264px; top:72px;"><span class="section-number">3</span><span class="section-label">Überschrift</span></div>
  <div class="section" style="left:92px; top:134px;"><span class="section-number">4</span><span class="section-label">Überschrift</span></div>
  <div class="section" style="left:177px; top:134px;"><span class="section-number">5</span><span class="section-label">Überschrift</span></div>
  <div class="section" style="left:264px; top:134px;"><span class="section-number">6</span><span class="section-label">Überschrift</span></div>
</section>

<section class="slide slide-text">
  <div class="slide-band"></div>
  <div class="card"></div>
  <div class="brand" style="left:281px; top:28px;"><span class="brand-mark"></span>PQ-KS<span class="brand-suffix">GmbH</span></div>
  <h2 class="heading">Überschrift</h2>
  <div class="body-text">
    <p>Lorem ipsum dolor sit amet, consetetur sadipscing elitr, sed diam nonumy eirmod tempor invidunt ut labore et dolore magna aliquyam erat, sed diam voluptua. At vero eos et accusam et justo duo dolores et ea rebum.</p>
    <p>Lorem ipsum dolor sit amet, consetetur sadipscing elitr, sed diam nonumy eirmod tempor invidunt ut labore et dolore magna aliquyam erat, sed diam voluptua. At vero eos et accusam et justo duo dolores et ea rebum.</p>
    <p>Lorem ipsum dolor sit amet, consetetur sadipscing elitr, sed diam nonumy eirmod tempor invidunt ut labore et dolore magna aliquyam erat, sed diam voluptua. At vero eos et accusam et justo duo dolores et ea rebum.</p>
    <p>Lorem ipsum dolor sit amet, consetetur sadipscing elitr, sed diam nonumy eirmod tempor invidunt ut labore et dolore magna aliquyam erat, sed diam voluptua. At vero eos et accusam et justo duo dolores et ea rebum.</p>
  </div>
</section>

<section class="slide slide-media">
  <div class="slide-band"></div>
  <div class="card"></div>
  <div class="photo" role="img" aria-label="Foto: Hände tippen auf einem Laptop auf einem Holztisch"></div>
  <div class="brand" style="left:285px; top:28px;"><span class="brand-mark"></span>PQ-KS<span class="brand-suffix">GmbH</span></div>
  <h2 class="heading">Überschrift</h2>
  <div class="body-text">
    <p>Lorem ipsum dolor sit amet, consetetur sadipscing elitr, sed diam nonumy eirmod tempor invidunt ut labore et dolore magna aliquyam erat, sed diam voluptua. At vero eos et accusam et justo duo dolores et ea rebum.</p>
    <p>Lorem ipsum dolor sit amet, consetetur sadipscing elitr, sed diam nonumy eirmod tempor invidunt ut labore et dolore magna aliquyam erat, sed diam voluptua. At vero eos et accusam et justo duo dolores et ea rebum.</p>
    <p>Lorem ipsum dolor sit amet, consetetur sadipscing elitr, sed diam nonumy eirmod tempor invidunt ut labore et dolore magna aliquyam erat, sed diam voluptua. At vero eos et accusam et justo duo dolores et ea rebum.</p>
    <p>Lorem ipsum dolor sit amet, consetetur sadipscing elitr, sed diam nonumy eirmod tempor invidunt ut labore et dolore magna aliquyam erat, sed diam voluptua. At vero eos et accusam et justo duo dolores et ea rebum.</p>
  </div>
</section>

<section class="slide slide-columns">
  <div class="slide-band"></div>
  <div class="brand" style="left:302px; top:10px;"><span class="brand-mark"></span>PQ-KS<span class="brand-suffix">GmbH</span></div>
  <div class="page" style="left:32px;">
    <div class="body-text">
      <p>Lorem ipsum dolor sit amet, consetetur sadipscing elitr, sed diam nonumy eirmod tempor invidunt ut labore et dolore magna aliquyam erat, sed diam voluptua. At vero eos et accusam et justo duo dolores et ea rebum.</p>
      <p>Lorem ipsum dolor sit amet, consetetur sadipscing elitr, sed diam nonumy eirmod tempor invidunt ut labore et dolore magna aliquyam erat, sed diam voluptua. At vero eos et accusam et justo duo dolores et ea rebum.</p>
      <p>Lorem ipsum dolor sit amet, consetetur sadipscing elitr, sed diam nonumy eirmod tempor invidunt ut labore et dolore magna aliquyam erat, sed diam voluptua. At vero eos et accusam et justo duo dolores et ea rebum.</p>
    </div>
  </div>
  <div class="page" style="left:199px;">
    <div class="body-text">
      <p>Lorem ipsum dolor sit amet, consetetur sadipscing elitr, sed diam nonumy eirmod tempor invidunt ut labore et dolore magna aliquyam erat, sed diam voluptua. At vero eos et accusam et justo duo dolores et ea rebum.</p>
      <p>Lorem ipsum dolor sit amet, consetetur sadipscing elitr, sed diam nonumy eirmod tempor invidunt ut labore et dolore magna aliquyam erat, sed diam voluptua. At vero eos et accusam et justo duo dolores et ea rebum.</p>
      <p>Lorem ipsum dolor sit amet, consetetur sadipscing elitr, sed diam nonumy eirmod tempor invidunt ut labore et dolore magna aliquyam erat, sed diam voluptua. At vero eos et accusam et justo duo dolores et ea rebum.</p>
    </div>
  </div>
</section>

</body>
</html>
```